Modern Business Card for Lanternfield 2018

Our company assumes the best about people. We are creating an online community of entrepreneurs and business leaders who struggle with marketing their business online.

This business card should POP! We recently got a new logo and are launching a new website next month, so our business cards should make a statement that feels:
-Fresh
-Smart
-Trustworthy
-Fun

Target Market(s)

small business owners, entrepreneurs

Industry/Entity Type

Digital Marketing

Contact Information for Business Card

Dimensions: 3.5" x 2"

Font styles to use
Sans Serif

Colors
f37122
ffffff

Requirements
Must have
• We need a business card with a modern, bold design. We will use one side of the card as a lead-generation offer, so text on one side will need to fit up to 140 characters. The business card should stick to our core colors (orange, black, and white).
Nice to have
• We think a vertical "portrait" design could be interesting.
Should not have
• Should not look like a traditional business card. The round icon should stand out from a distance.

```html
<!DOCTYPE html>
<html lang="en">
<head>
<meta charset="utf-8">
<title>Lanternfield Business Card – Dana Whitlow</title>
<link rel="stylesheet" href="https://fonts.googleapis.com/css2?family=Open+Sans:wght@400&family=Permanent+Marker&family=Ubuntu:wght@700&display=swap">
<style>
  :root {
    --brand-orange: #f37122;
    --mark-tint: #f6aa78;
    --mark-soft: #ffc996;
    --ink: #000000;
    --paper: #ffffff;
  }
  html, body {
    margin: 0;
    padding: 0;
    width: 982px;
    height: 1200px;
    overflow: hidden;
    background: var(--paper);
  }
  .card-sheet {
    display: block;
    width: 982px;
    height: 1200px;
  }
  .card-edge { fill: var(--paper); stroke: var(--ink); stroke-width: 3; }
  .top-band { fill: var(--brand-orange); }
  .wave-stripe { fill: none; stroke: var(--brand-orange); stroke-width: 10; }
  .badge-circle { fill: var(--mark-tint); }
  .badge-circle--back { fill: var(--mark-soft); }
  .job-title {
    font-family: "Ubuntu", sans-serif;
    font-weight: 700;
    font-size: 32px;
    letter-spacing: 1px;
    fill: var(--ink);
  }
  .person-name {
    font-family: "Permanent Marker", cursive;
    font-size: 92px;
    fill: var(--ink);
  }
  .brand-name {
    font-family: "Ubuntu", sans-serif;
    font-weight: 700;
    font-size: 30px;
    fill: var(--brand-orange);
  }
  .contact-email {
    font-family: "Open Sans", sans-serif;
    font-size: 36px;
    fill: var(--ink);
  }
</style>
</head>
<body>
<svg class="card-sheet" viewBox="0 0 1054 1288" preserveAspectRatio="none" xmlns="http://www.w3.org/2000/svg" role="img" aria-label="Front and back of the Lanternfield business card for Dana Whitlow">
  <defs>
    <clipPath id="front-clip"><rect x="3" y="3" width="1049" height="599"/></clipPath>
  </defs>

  <!-- Front side -->
  <g class="card-front">
    <rect class="card-edge" x="3" y="3" width="1049" height="599"/>
    <g clip-path="url(#front-clip)">
      <path class="top-band" d="M0,0 H1054 V300 C980,360 910,390 840,422 C740,468 620,480 520,462 C400,442 330,402 268,374 C180,338 80,318 0,330 Z"/>
      <path class="wave-stripe" d="M0,347 C100,330 200,350 300,396 C420,452 520,490 640,488 C760,486 860,432 1054,322"/>
    </g>
    <circle class="badge-circle" cx="551" cy="270" r="165"/>
    <text class="job-title" x="527" y="82" text-anchor="middle">STORY MARKETING COACH</text>
    <text class="person-name" x="552" y="328" text-anchor="middle">DANA WHITLOW</text>
    <text class="brand-name" x="551" y="392" text-anchor="middle">Lanternfield</text>
    <text class="contact-email" x="527" y="546" text-anchor="middle">dana@lanternfieldnow.com</text>
  </g>

  <!-- Back side -->
  <g class="card-back">
    <rect class="card-edge" x="3" y="686" width="1049" height="599"/>
    <circle class="badge-circle--back" cx="527" cy="975" r="102"/>
    <text class="brand-name" x="527" y="1125" text-anchor="middle">Lanternfield</text>
  </g>
</svg>
</body>
</html>
```